R J Penn Accounting & SMSF Auditing needs a Web Site Design

I need some examples of what a web design can look like for my business.
The business name is above and I have already registered a domain name of www.penn-smsf.com.au
I have attached my current letterhead and business cards and would like to maintain these colours basically Red on White with some black

```html
<!DOCTYPE html>
<html lang="en">
<head>
<meta charset="utf-8">
<title>R J Penn Accounting &amp; SMSF Auditing</title>
<link rel="stylesheet" href="https://fonts.googleapis.com/css2?family=Arimo:ital,wght@0,400;0,700;1,400&family=Roboto+Condensed:wght@700&display=swap">
<style>
:root{
  --red:#c0112a;
  --ink:#333333;
  --muted:#555555;
  --nav:#3a3a3a;
  --nav-line:#555555;
  --rule:#dddddd;
  --footer:#2b2b2b;
  --footer-base:#1f1f1f;
  --footer-text:#bdbdbd;
  --white:#ffffff;
}
*{box-sizing:border-box;margin:0;padding:0}
html,body{width:1037px;height:1200px;overflow:hidden;background:var(--white)}
body{position:relative;font-family:"Arimo",Arial,sans-serif;color:var(--ink)}
.abs{position:absolute}
.brand{left:0;width:1037px;top:34px;text-align:center;font-size:29px;color:var(--red);font-weight:400;letter-spacing:.5px}
.brand-sub{left:0;width:1037px;top:72px;text-align:center;font-size:16px;color:#444;letter-spacing:.5px}
.nav{left:155px;top:116px;width:727px;height:38px;background:var(--nav);display:flex}
.nav a{display:flex;align-items:center;justify-content:center;color:var(--white);font-size:10.5px;text-decoration:none;border-right:1px solid var(--nav-line)}
.nav a:last-child{border-right:0}
.nav a.active{background:var(--red)}
.hero{left:155px;top:154px;width:727px;height:286px;background:linear-gradient(90deg,#d9d0c4 0%,#cfc2b1 30%,#eeeeee 58%,#f6f6f6 100%)}
.hero-title{left:558px;top:216px;font-size:32px;color:var(--red)}
.hero-sub{left:558px;top:257px;font-size:21px;color:#222}
.hero-text{left:558px;top:290px;width:290px;font-size:11px;line-height:19px;color:var(--muted)}
.btn{display:flex;align-items:center;justify-content:center;background:var(--red);color:var(--white);font-size:11px;border-radius:2px}
.hero-btn{left:560px;top:342px;width:163px;height:36px;font-size:12px}
.arrows{left:828px;top:402px;display:flex;gap:1px}
.arrows span{width:20px;height:20px;background:#b8b8b8;display:flex;align-items:center;justify-content:center}
.heading{font-family:"Roboto Condensed",Arial,sans-serif;font-weight:700;font-size:16px;color:#2a2a2a;text-transform:uppercase}
.mini-arrows{display:flex;gap:6px}
.photo{border-radius:0}
.lead{font-size:10px;line-height:18px;color:#222}
.copy{font-size:9px;line-height:17.5px;color:var(--muted)}
.news{left:438px;width:204px;height:78px;border-bottom:1px solid var(--rule)}
.news .thumb{position:absolute;left:0;top:0;width:64px;height:60px;border:2px solid #e8e8e8}
.news .title{position:absolute;left:79px;top:3px;font-size:9.5px;color:var(--red)}
.news .date{position:absolute;left:79px;top:19px;font-size:9px;font-style:italic;color:var(--muted)}
.news .text{position:absolute;left:79px;top:33px;font-size:9px;line-height:15.5px;color:var(--muted)}
.quote{left:624px;top:822px;width:258px;height:94px;background:#ececec;border:1px solid #dcdcdc;border-radius:3px;padding:22px 18px 0 26px;font-size:9px;font-style:italic;line-height:17.5px;color:var(--muted)}
.footer{left:0;top:999px;width:1037px;height:157px;background:var(--footer)}
.footer-base{left:0;top:1156px;width:1037px;height:44px;background:var(--footer-base);color:var(--footer-text);font-size:9px;text-align:center;line-height:44px}
.flinks{font-size:9px;line-height:19.2px;color:var(--footer-text);list-style:none}
.fhead{font-size:9.5px;font-weight:700;color:var(--white)}
.finfo{font-size:9px;color:var(--footer-text)}
.social{display:flex;align-items:center;gap:6px;font-size:9px;color:var(--footer-text)}
.social i{width:24px;height:24px;border-radius:50%;background:#5a5a5a;display:block}
</style>
</head>
<body>

<header>
  <div class="abs brand">R J Penn Accounting &amp; SMSF Auditing</div>
  <div class="abs brand-sub">Kessington Penn Pty Ltd T/A</div>
</header>

<nav class="abs nav">
  <a class="active" style="width:104px">HOME</a>
  <a style="width:111px">ABOUT US</a>
  <a style="width:113px">SERVICES</a>
  <a style="width:137px">TESTIMONIALS</a>
  <a style="width:127px">EXPERIENCE</a>
  <a style="width:135px">CONTACT US</a>
</nav>

<section class="abs hero" role="img" aria-label="Portrait of a smiling accountant in glasses and a light suit"></section>
<h1 class="abs hero-title" style="font-weight:400">Robert J. Penn</h1>
<div class="abs hero-sub">Accounting and Auditing firm</div>
<p class="abs hero-text">Lorem Ipsum is simply dummy text of the printing and type-setting industry. Lorem Ipsum has been the industry's</p>
<div class="abs btn hero-btn">Click here for more info</div>
<div class="abs arrows">
  <span><svg width="8" height="10" viewBox="0 0 8 10"><path d="M6 1 2 5l4 4" fill="none" stroke="#fff" stroke-width="1.3"/></svg></span>
  <span><svg width="8" height="10" viewBox="0 0 8 10"><path d="M2 1l4 4-4 4" fill="none" stroke="#fff" stroke-width="1.3"/></svg></span>
</div>

<!-- Welcome -->
<h2 class="abs heading" style="left:155px;top:472px">Welcome to Accounting &amp; SMSF</h2>
<div class="abs photo" style="left:155px;top:507px;width:251px;height:125px;background:linear-gradient(135deg,#d8d8d8,#8a8a8a 60%,#3a3a3a)" role="img" aria-label="Two colleagues reviewing documents at a desk"></div>
<p class="abs lead" style="left:155px;top:645px;width:251px">Lorem Ipsum is simply dummy text of the printing and typesetting industry.</p>
<p class="abs copy" style="left:155px;top:688px;width:251px">Lorem Ipsum is simply dummy text of the printing and typeset-ting industry. Lorem Ipsum has been the industry's standard dummy text ever since the 1500s...</p>

<!-- News -->
<h2 class="abs heading" style="left:438px;top:472px">Latest News</h2>
<div class="abs mini-arrows" style="left:611px;top:477px">
  <svg width="6" height="9" viewBox="0 0 6 9"><path d="M5 1 1.5 4.5 5 8" fill="none" stroke="#777" stroke-width="1.2"/></svg>
  <svg width="6" height="9" viewBox="0 0 6 9"><path d="M1 1l3.5 3.5L1 8" fill="none" stroke="#777" stroke-width="1.2"/></svg>
</div>
<article class="abs news" style="top:510px">
  <div class="thumb" style="background:linear-gradient(135deg,#9aa0a8,#3e4650)" role="img" aria-label="Business people shaking hands in a meeting"></div>
  <div class="title">LOREM IPSUM IS SIMPLY</div>
  <div class="date">Posted on 27 March 2014</div>
  <div class="text">Lorem Ipsum is simply dummy<br>text of the printing...</div>
</article>
<article class="abs news" style="top:597px">
  <div class="thumb" style="background:linear-gradient(135deg,#e0c3ad,#4a4f58)" role="img" aria-label="Hands typing on a keyboard"></div>
  <div class="title">LOREM IPSUM IS SIMPLY</div>
  <div class="date">Posted on 27 March 2014</div>
  <div class="text">Lorem Ipsum is simply dummy<br>text of the printing...</div>
</article>
<article class="abs news" style="top:684px;border-bottom:0">
  <div class="thumb" style="background:linear-gradient(135deg,#f2e6d6,#b58a66)" role="img" aria-label="Close-up of a handshake"></div>
  <div class="title">LOREM IPSUM IS SIMPLY</div>
  <div class="date">Posted on 27 March 2014</div>
  <div class="text">Lorem Ipsum is simply dummy<br>text of the printing...</div>
</article>

<!-- Experience -->
<h2 class="abs heading" style="left:678px;top:472px">Experience</h2>
<div class="abs photo" style="left:678px;top:507px;width:203px;height:110px;background:linear-gradient(135deg,#b9c8d6,#d9c3ae 55%,#7d8a99)" role="img" aria-label="Advisor talking with a couple at a laptop"></div>
<p class="abs copy" style="left:678px;top:630px;width:203px">Lorem Ipsum is simply dummy text of the printing and typesetting industry. Lorem Ipsum has been the industry's standard dummy text ever since the 1500s, when an unknown printer...</p>
<div class="abs btn" style="left:678px;top:712px;width:109px;height:26px">Read more info</div>

<!-- About -->
<h2 class="abs heading" style="left:155px;top:794px">About Accounting &amp; SMSF</h2>
<div class="abs photo" style="left:155px;top:830px;width:191px;height:122px;background:linear-gradient(135deg,#c99a7a,#efe9e2 45%,#7a7d84)" role="img" aria-label="Hands pointing at a printed bar chart beside a laptop"></div>
<p class="abs copy" style="left:370px;top:825px;width:222px">Lorem Ipsum is simply dummy text of the printing and typesetting industry. Lorem Ipsum has been the indus-try's standard dummy text ever since the 1500s, when an unknown printer took a galley of type and scrambled it to make a type specimen book.</p>
<div class="abs btn" style="left:370px;top:924px;width:109px;height:26px">Read more info</div>

<!-- Testimonials -->
<h2 class="abs heading" style="left:624px;top:792px">Testimonials</h2>
<div class="abs mini-arrows" style="left:858px;top:797px">
  <svg width="6" height="9" viewBox="0 0 6 9"><path d="M5 1 1.5 4.5 5 8" fill="none" stroke="#777" stroke-width="1.2"/></svg>
  <svg width="6" height="9" viewBox="0 0 6 9"><path d="M1 1l3.5 3.5L1 8" fill="none" stroke="#777" stroke-width="1.2"/></svg>
</div>
<blockquote class="abs quote">Lorem Ipsum is simply dummy text of the printing and typesetting industry. Lorem Ipsum has been the indus-try's standard dummy text ever since...</blockquote>
<svg class="abs" style="left:798px;top:915px" width="36" height="19" viewBox="0 0 36 19"><path d="M0 0h36L2 18z" fill="#ececec" stroke="#dcdcdc"/><path d="M1 0h34" stroke="#ececec" stroke-width="2"/></svg>
<div class="abs" style="left:626px;top:929px;width:37px;height:37px;border:2px solid #e3e3e3;background:linear-gradient(135deg,#c9b9a9,#4b4f57)" role="img" aria-label="Client portrait"></div>
<div class="abs" style="left:679px;top:930px;font-size:10px;color:var(--red)">Marcus Fellow</div>
<div class="abs" style="left:679px;top:947px;font-size:8px;color:#777">Marketing Executive</div>

<!-- Footer -->
<footer class="abs footer">
  <ul class="abs flinks" style="left:190px;top:20px">
    <li>Home</li><li>About Us</li><li>Services</li><li>Testimonials</li><li>Experience</li><li>Contact us</li>
  </ul>
  <ul class="abs flinks" style="left:316px;top:20px">
    <li>Terms &amp; Regards</li><li>Privacy Policy</li><li>Disclaimer</li>
  </ul>
  <div class="abs fhead" style="left:464px;top:25px">ROBERT J. PENN</div>
  <div class="abs finfo" style="left:464px;top:46px">PO Box 718 Riverton WA 6148</div>
  <div class="abs finfo" style="left:464px;top:68px;display:flex;align-items:center;gap:6px">
    <svg width="10" height="10" viewBox="0 0 10 10"><path d="M2 0.5 3.8 2.6 2.8 3.8Q4 6.3 6.2 7.2L7.4 6.2 9.5 8 8.3 9.5Q2.5 8.7 0.5 1.7z" fill="#bdbdbd"/></svg>0400 555 219</div>
  <div class="abs finfo" style="left:464px;top:91px;display:flex;align-items:center;gap:6px">
    <svg width="10" height="8" viewBox="0 0 10 8"><rect x=".5" y=".5" width="9" height="7" fill="none" stroke="#bdbdbd"/><path d="M.5.5 5 4.5 9.5.5" fill="none" stroke="#bdbdbd"/></svg>robertpenn@pennmail.net.au</div>
  <div class="abs fhead" style="left:664px;top:25px">FOLLOW US</div>
  <div class="abs social" style="left:664px;top:48px"><i></i>: Friendspace</div>
  <div class="abs social" style="left:775px;top:48px"><i></i>: Chirper</div>
  <div class="abs social" style="left:664px;top:87px"><i></i>: Workednet</div>
  <div class="abs social" style="left:775px;top:87px"><i></i>: Circleplus</div>
</footer>
<div class="abs footer-base">Copyrights &nbsp;@2014. Accounting &amp; SMSF. All Rights Reserved</div>

</body>
</html>
```